Artwork for a CD cover

I'm after a 4 panel Digifile CD cover with matching print or logo on the CD. I have the wording prepared on a mock up which is in the accompanying file, which is set up with a (place holder) cover image, giving wording in a mock up and some very basic ideas I have. But I welcome and design ideas you might have. The music is improvised jazz, with a melodic flowing quality

```html
<!DOCTYPE html>
<html lang="en">
<head>
<meta charset="utf-8">
<title>Ashcroft, Mercer, Hale and Calloway – Digifile Artwork</title>
<link rel="stylesheet" href="https://fonts.googleapis.com/css2?family=Anton&family=Arimo:wght@400;700&family=Cousine&family=Great+Vibes&display=swap">
<style>
  :root{
    --sky:#f2c9c6;
    --sky-light:#f6dcd6;
    --sea-deep:#2f6670;
    --sea:#5d8f95;
    --foam:#dfe6e2;
    --sand-light:#efd8c4;
    --sand:#dba57c;
    --sand-deep:#d08f5e;
    --ink:#111;
    --teal-type:#245e6a;
    --white:#fff;
    --trim:#1d2f6a;
  }
  *{box-sizing:border-box;margin:0;padding:0}
  html,body{width:1003px;height:1200px;overflow:hidden;background:#fff}
  .canvas{position:relative;width:1003px;height:1200px;font-family:"Arimo",Arial,sans-serif}
  .panel{position:absolute;overflow:hidden;border:1px solid #222}
  .scene{position:absolute;inset:0}

  /* outer spread */
  .back-panel{left:24px;top:100px;width:461px;height:464px}
  .back-panel .trim{position:absolute;left:13px;top:0;bottom:0;border-left:1px solid var(--trim)}
  .back-panel .scene{background:linear-gradient(180deg,var(--sky-light) 0%,var(--sky) 35%,var(--sea-deep) 36%,var(--sea) 45%,var(--foam) 58%,var(--sea) 66%,var(--foam) 78%,var(--sand-light) 84%,var(--sand) 100%)}
  .spine{left:485px;top:100px;width:13px;height:464px;border-color:var(--trim)}
  .spine .scene{background:linear-gradient(180deg,var(--sky) 0%,var(--sky) 35%,var(--sea-deep) 36%,var(--foam) 70%,var(--sand) 100%)}
  .spine-title{position:absolute;left:0;width:11px;top:142px;writing-mode:vertical-rl;white-space:nowrap;font-size:7.6px;line-height:11px;font-weight:700;color:var(--white);letter-spacing:.2px;-webkit-text-stroke:.25px var(--teal-type);text-align:center}
  .front-panel{left:499px;top:100px;width:459px;height:464px}
  .front-panel .scene{background:linear-gradient(180deg,var(--sky-light) 0%,var(--sky) 50%,var(--sea-deep) 51%,var(--sea) 62%,var(--foam) 80%,var(--sea) 90%,var(--foam) 100%)}
  .portrait-area{position:absolute;left:80px;top:20px;width:360px;height:440px;border-radius:40% 40% 8% 8%;background:radial-gradient(ellipse at 50% 40%,rgba(255,240,235,.35),rgba(255,240,235,0) 70%)}

  .playlist-title{position:absolute;left:0;right:0;top:26px;text-align:center;font-family:"Cousine",monospace;font-weight:400;font-size:16px;letter-spacing:1px;color:var(--ink)}
  .tracks{position:absolute;left:70px;top:55px;width:328px;list-style:none;font-size:9.6px;color:var(--ink)}
  .tracks li{display:flex;line-height:12.2px;white-space:nowrap}
  .tracks .credit{font-size:7.2px}
  .tracks .dots{flex:1;overflow:hidden;margin:0 2px}
  .tracks .dots::after{content:"....................................................................................................";letter-spacing:.5px}
  .tracks .time{width:26px;text-align:right}

  .lineup{position:absolute;left:163px;top:351px;font-size:8.6px;font-weight:700;line-height:10.4px;color:var(--teal-type);list-style:none}
  .site,.rights{position:absolute;left:0;right:0;text-align:center;font-size:7.8px;font-weight:700;color:var(--teal-type)}
  .site{top:421px}
  .rights{top:439px}

  .cover-title{position:absolute;left:27px;top:258px;font-family:"Anton",Impact,sans-serif;font-weight:400;font-size:33px;line-height:39.5px;color:var(--teal-type);letter-spacing:.2px}

  /* inner spread */
  .inner-left{left:31px;top:651px;width:461px;height:465px}
  .inner-right{left:492px;top:651px;width:459px;height:462px;border-left:none}
  .inner-left .scene,.inner-right .scene{background:linear-gradient(180deg,var(--sky-light) 0%,var(--sky) 33%,var(--sea-deep) 34%,var(--sea) 48%,var(--foam) 58%,var(--sea) 66%,var(--foam) 76%,var(--sand-light) 80%,var(--sand) 88%,var(--sand-deep) 100%)}
  .fold-guide{position:absolute;right:0;top:0;bottom:0;width:20px;border-left:1px solid var(--white)}
  .band-photos{position:absolute;left:88px;top:207px;width:281px;height:69px;background:linear-gradient(90deg,#3b2416 0%,#6a3c22 30%,#2a1a12 48%,#d9d4cc 52%,#3a2a22 60%,#5a2e26 100%)}
  .thanks{position:absolute;left:10px;right:10px;top:325px;text-align:center;font-family:"Great Vibes",cursive;font-size:16.5px;line-height:19.7px;color:var(--white)}
</style>
</head>
<body>
<main class="canvas">

  <section class="panel back-panel">
    <div class="scene" role="img" aria-label="Photograph of a pink-sky beach with a woman standing in the shallow surf"></div>
    <div class="trim"></div>
    <h2 class="playlist-title">PLAYLIST</h2>
    <ol class="tracks">
      <li><span class="name">SEA GLASS <span class="credit">(ASHCROFT)</span></span><span class="dots"></span><span class="time">7:12</span></li>
      <li><span class="name">KINGFISHER <span class="credit">(HALE)</span></span><span class="dots"></span><span class="time">4:38</span></li>
      <li><span class="name">EVENING TIDE (SANDPIPER SONG) <span class="credit">(ASHCROFT)</span></span><span class="dots"></span><span class="time">6:21</span></li>
      <li><span class="name">WE ARE THE SHORE, WE ARE THE LIGHT <span class="credit">(ASHCROFT)</span></span><span class="dots"></span><span class="time">3:47</span></li>
      <li><span class="name">HLM 7 <span class="credit">(CALLOWAY)</span></span><span class="dots"></span><span class="time">5:56</span></li>
      <li><span class="name">ONE MORE WALTZ <span class="credit">(MERCER)</span></span><span class="dots"></span><span class="time">3:09</span></li>
      <li><span class="name">CRISP <span class="credit">(ASHCROFT)</span></span><span class="dots"></span><span class="time">3:02</span></li>
    </ol>
    <ul class="lineup">
      <li>TOM ASHCROFT – double bass</li>
      <li>SAM MERCER &nbsp;– drumkit</li>
      <li>LUCA HALE &nbsp;&nbsp;– tenor saxophone</li>
      <li>OWEN CALLOWAY – piano</li>
    </ul>
    <p class="site">www.tomashcroft.com.au</p>
    <p class="rights">All rights reserved Copyright Tidewater Music 2022</p>
  </section>

  <section class="panel spine">
    <div class="scene" role="img" aria-label="Continuation of the beach photograph across the spine"></div>
    <p class="spine-title">ASHCROFT, MERCER, HALE and CALLOWAY</p>
  </section>

  <section class="panel front-panel">
    <div class="scene" role="img" aria-label="Beach seascape under a pink sky"></div>
    <div class="portrait-area" role="img" aria-label="Faint illustration of a trumpet player blended over the sky and sea"></div>
    <h1 class="cover-title">TOM ASHCROFT<br>MERCER<br>HALE<br>CALLOWAY</h1>
  </section>

  <section class="panel inner-left">
    <div class="scene" role="img" aria-label="Sunlit beach seascape with faint musician figures in the sky"></div>
    <div class="fold-guide"></div>
    <div class="band-photos" role="img" aria-label="Strip of live performance photographs of the quartet"></div>
    <p class="thanks">Tom Ashcroft would like to thank Sam, Luca and<br>Owen for their encouragement and superb musicianship.<br>Thanks to my family and all of the musicians I play with who<br>have made me the player I am. Many thanks to the Southern<br>Coast Arts Council for financial support of this project</p>
  </section>

  <section class="panel inner-right">
    <div class="scene" role="img" aria-label="Sunlit beach seascape with faint musician figures in the sky"></div>
  </section>

</main>
</body>
</html>
```